Business Card Design

I need a business card designed for my business.

The company name is Rowan Pellet Group

It has four brands underneath it. They are:
- RP Events
- RP Sports Tours
- RPG Management
- Bold Mosaic

I have attached all logo items, as well as our last business card.

I look forward to seeing your designs.

Industry/Entity Type

Business

Colors
eb1f27
0355a3

Requirements
Must have
• Our contact details as per the front page of our previous business card.

```html
<!DOCTYPE html>
<html lang="en">
<head>
<meta charset="utf-8">
<title>Rowan Pellet Group – Business Card</title>
<link rel="stylesheet" href="https://fonts.googleapis.com/css2?family=Montserrat:wght@400;600;700;800&display=swap">
<style>
  :root {
    --stage: #1c1c1c;
    --white: #ffffff;
    --brand-blue: #0355a3;
    --brand-red: #eb1f27;
    --sky: #1a9be0;
    --ink: #0a3f86;
    --soft-blue: #dbe8f5;
  }
  * { margin: 0; padding: 0; box-sizing: border-box; }
  html, body { width: 847px; height: 1200px; overflow: hidden; }
  body {
    background: var(--stage);
    font-family: "Montserrat", sans-serif;
    position: relative;
  }

  /* Wordmark header */
  .wordmark {
    position: absolute; left: 0; right: 0; top: 145px;
    display: flex; justify-content: center; align-items: center; gap: 18px;
    color: var(--white);
  }
  .wordmark__dot { width: 78px; height: 78px; border-radius: 50%; background: var(--white); }
  .wordmark__name { font-weight: 800; font-size: 44px; letter-spacing: -1px; line-height: 1; }
  .wordmark__sub {
    font-weight: 800; font-size: 26px; line-height: 1; text-align: right;
    margin-top: 6px; display: flex; align-items: center; gap: 10px;
  }
  .wordmark__sub::before { content: ""; flex: 1; height: 3px; background: var(--white); }

  /* Cards */
  .card {
    position: absolute; left: 180px; width: 487px; height: 278px;
    overflow: hidden; box-shadow: 0 8px 18px rgba(0,0,0,.6);
  }
  .card--front { top: 353px; background: var(--white); }
  .card--back {
    top: 766px;
    background: radial-gradient(ellipse at 50% 40%, #2fb0ef 0%, var(--sky) 35%, var(--brand-blue) 100%);
  }

  /* Front */
  .front__logo {
    position: absolute; left: 22px; top: 26px;
    display: flex; align-items: center; gap: 8px;
    color: var(--brand-blue); font-weight: 800; font-size: 14px; line-height: 1.05;
  }
  .front__logo-dot { width: 28px; height: 28px; border-radius: 50%; background: var(--brand-red); }
  .front__logo small { display: block; font-size: 9px; text-align: right; }
  .front__band {
    position: absolute; left: 207px; right: 0; top: 23px; height: 44px;
    background: var(--brand-blue); color: var(--white);
    padding: 6px 0 0 55px;
  }
  .front__name { font-weight: 700; font-size: 17px; letter-spacing: .5px; line-height: 1.1; }
  .front__role { font-weight: 600; font-size: 9px; letter-spacing: 2px; }
  .front__address {
    position: absolute; left: 22px; top: 124px;
    font-size: 10px; font-weight: 600; color: var(--ink);
  }
  .front__contacts {
    position: absolute; left: 22px; top: 174px; list-style: none;
    font-size: 10px; font-weight: 600; color: var(--ink);
  }
  .front__contacts li { display: flex; align-items: center; gap: 6px; height: 22.5px; }
  .front__contacts svg { width: 13px; height: 13px; fill: var(--ink); flex: none; }
  .front__artwork {
    position: absolute; left: 290px; top: 90px; right: 14px; bottom: 14px;
    background: linear-gradient(160deg, var(--soft-blue), #c7d9ee);
  }

  /* Back */
  .back__logo {
    position: absolute; left: 0; right: 0; top: 92px;
    display: flex; justify-content: center; align-items: center; gap: 10px;
    color: var(--white);
  }
  .back__logo-dot { width: 42px; height: 42px; border-radius: 50%; background: var(--white); }
  .back__logo-name { font-weight: 800; font-size: 24px; letter-spacing: -.5px; line-height: 1; }
  .back__logo-sub {
    font-weight: 800; font-size: 13px; display: flex; align-items: center; gap: 6px; margin-top: 3px;
  }
  .back__logo-sub::before { content: ""; flex: 1; height: 2px; background: var(--white); }
  .back__tagline {
    position: absolute; left: 0; right: 0; top: 194px; text-align: center;
    color: var(--white); font-size: 13px; font-weight: 600; letter-spacing: .5px;
  }
  .back__brands {
    position: absolute; left: 0; right: 0; bottom: 0; height: 56px;
    background: var(--white); display: flex; justify-content: space-around; align-items: center;
    list-style: none; padding: 0 10px;
  }
  .back__brands li { font-size: 12px; font-weight: 700; color: var(--brand-blue); }
  .back__brands li:nth-child(2), .back__brands li:nth-child(4) { color: var(--brand-red); }
</style>
</head>
<body>

<header class="wordmark">
  <span class="wordmark__dot"></span>
  <div>
    <div class="wordmark__name">ROWAN PELLET</div>
    <div class="wordmark__sub">GROUP</div>
  </div>
</header>

<section class="card card--front" aria-label="Card front">
  <div class="front__logo">
    <span class="front__logo-dot"></span>
    <div>ROWAN PELLET<small>GROUP</small></div>
  </div>
  <div class="front__band">
    <div class="front__name">ROWAN PELLET</div>
    <div class="front__role">PRINCIPAL</div>
  </div>
  <p class="front__address">PO Box 418 Halden ACT 2690 Australia</p>
  <ul class="front__contacts">
    <li><svg viewBox="0 0 24 24"><path d="M6.6 10.8a15 15 0 0 0 6.6 6.6l2.2-2.2a1 1 0 0 1 1-.25 11.4 11.4 0 0 0 3.6.57 1 1 0 0 1 1 1V20a1 1 0 0 1-1 1A17 17 0 0 1 3 4a1 1 0 0 1 1-1h3.5a1 1 0 0 1 1 1c0 1.25.2 2.45.57 3.6a1 1 0 0 1-.25 1z"/></svg>+61 2 6200 4815</li>
    <li><svg viewBox="0 0 24 24"><path d="M6.6 10.8a15 15 0 0 0 6.6 6.6l2.2-2.2a1 1 0 0 1 1-.25 11.4 11.4 0 0 0 3.6.57 1 1 0 0 1 1 1V20a1 1 0 0 1-1 1A17 17 0 0 1 3 4a1 1 0 0 1 1-1h3.5a1 1 0 0 1 1 1c0 1.25.2 2.45.57 3.6a1 1 0 0 1-.25 1z"/></svg>+61 455 203 918</li>
    <li><svg viewBox="0 0 24 24"><path d="M2 5h20v14H2z M2 5l10 8 10-8" fill="none" stroke="#0a3f86" stroke-width="2.4"/></svg>rowan@rowanpelletgroup.com.au</li>
    <li><svg viewBox="0 0 24 24"><circle cx="12" cy="12" r="10"/><path d="M2 12h20M12 2c3 3 3 17 0 20M12 2c-3 3-3 17 0 20" fill="none" stroke="#fff" stroke-width="1.4"/></svg>www.rowanpelletgroup.com.au</li>
  </ul>
  <div class="front__artwork" role="img" aria-label="Space for the group's large brand artwork"></div>
</section>

<section class="card card--back" aria-label="Card back">
  <div class="back__logo">
    <span class="back__logo-dot"></span>
    <div>
      <div class="back__logo-name">ROWAN PELLET</div>
      <div class="back__logo-sub">GROUP</div>
    </div>
  </div>
  <p class="back__tagline">Event, Travel And Talent Management</p>
  <ul class="back__brands">
    <li>RP Events</li>
    <li>RP Sports Tours</li>
    <li>RPG Management</li>
    <li>Bold Mosaic</li>
  </ul>
</section>

</body>
</html>
```